Fancy flyer to entice High School Students

http://tarnvelsw.com needs a marketing slick/flyer to pass out. The marketing text is below(feel free to place where you think appropriate).

* 8th grade to 12th grade (or 8th graders to 12th graders)
* Land a real job internship(instead of Krovetts)
* 100's of internships available
* Learn how to start your own business out of High School making way more than minimum wage
* In college when interviewing for an internship don't be the guy that answers "no, sorry, this would be my first internship" putting you at a huge disadvantage"
* Fill in the Contact Us form at http://tarnvelsw.com at the bottom left corner to find out more information

We will be evaluating design with this blog post in mind....
http://yourpostingpulse.com/color-influence-buyers/

We like attention grabbing contact us type stuff and calls to action. If you feel it is appropriate to change the marketing text to make your flyer stand out, please feel free. I am not the best at marketing and am the first to admit it.
Updates

A simple 8.5 x 11 flyer would be great.

Target Market(s)

High School students, male and female with high grade point averages(smart students). For the top 20% of their class.

Industry/Entity Type

Marketing

Requirements
Must have
• good call to action

```html
<!DOCTYPE html>
<html lang="en">
<head>
<meta charset="utf-8">
<title>Tarnvel Software – Internship Flyer</title>
<link rel="stylesheet" href="https://fonts.googleapis.com/css2?family=Cabin+Sketch:wght@700&family=PT+Sans:wght@400;700&display=swap">
<style>
  :root {
    --blue-deep: #0f4a66;
    --blue-mid: #1b6f8f;
    --blue-light: #2f8fae;
    --orange: #f5a21a;
    --orange-deep: #e9851a;
    --olive: #8d8f1c;
    --yellow: #f3c52a;
    --ink: #1c1a14;
    --shadow-ink: #0d0d0d;
    --bullet: #1f4f8a;
    --paper: #f7f7f5;
    --pill-red: #e2583a;
    --pill-edge: #f4d7cc;
    --logo-grey: #2b2b2b;
    --white: #ffffff;
  }
  * { box-sizing: border-box; margin: 0; padding: 0; }
  html, body { width: 928px; height: 1200px; overflow: hidden; background: var(--paper); }
  .flyer {
    position: relative; width: 928px; height: 1200px; overflow: hidden;
    font-family: "PT Sans", Arial, sans-serif; color: var(--ink);
  }
  .band-warm {
    position: absolute; left: 0; top: 400px; width: 928px; height: 674px;
    background:
      radial-gradient(ellipse at 30% 40%, var(--yellow) 0%, rgba(243,197,42,0) 55%),
      linear-gradient(110deg, var(--orange-deep) 0%, var(--orange) 35%, #d6a61f 65%, var(--olive) 100%);
  }
  .band-cool { position: absolute; left: 0; top: 0; width: 928px; height: 450px; }
  .headline-panel {
    position: absolute; left: 24px; top: 36px; width: 660px; height: 345px;
    background: linear-gradient(160deg, rgba(47,143,174,0.55), rgba(27,111,143,0.25));
    border: 3px solid rgba(120,190,210,0.35);
  }
  .headline {
    position: absolute; left: 72px; top: 96px; transform: rotate(-3deg); transform-origin: left top;
    font-family: "Cabin Sketch", "Comic Sans MS", cursive; font-weight: 700;
    font-size: 55px; line-height: 63px; letter-spacing: 2px; text-transform: uppercase;
    color: var(--white); text-shadow: 2px 2px 0 rgba(0,0,0,0.25);
  }
  .figure {
    position: absolute;
    background: linear-gradient(180deg, var(--shadow-ink), #1a1a1a);
    border-radius: 40px 40px 10px 10px;
  }
  .figure--standing-man { left: 690px; top: 52px; width: 140px; height: 485px; }
  .figure--walking-woman { left: 118px; top: 526px; width: 94px; height: 382px; }
  .figure--pair { left: 752px; top: 856px; width: 88px; height: 162px; }
  .points { position: absolute; left: 288px; top: 553px; width: 500px; list-style: none; }
  .points li {
    position: relative; padding-left: 34px; margin-bottom: 18px;
    font-size: 22px; line-height: 26px;
  }
  .points li::before {
    content: ""; position: absolute; left: 0; top: 6px; width: 14px; height: 14px; background: var(--bullet);
  }
  .points b { font-weight: 700; }
  .points .big { font-size: 34px; line-height: 32px; font-weight: 700; }
  .cta-lead {
    position: absolute; left: 82px; top: 1028px; color: var(--white); font-size: 17px;
  }
  .footer { position: absolute; left: 0; top: 1074px; width: 928px; height: 126px; background: var(--paper); }
  .url-pill {
    position: absolute; left: 66px; top: 1062px; width: 268px; height: 44px;
    border-radius: 22px; border: 4px solid var(--pill-edge);
    background: linear-gradient(180deg, #f07a5a, var(--pill-red));
    color: var(--white); font-size: 21px; line-height: 36px; text-align: center;
  }
  .cta-note { position: absolute; left: 67px; top: 1116px; font-size: 11px; color: var(--logo-grey); }
  .brand {
    position: absolute; left: 556px; top: 1094px; display: flex; align-items: center; gap: 10px;
    font-size: 32px; font-weight: 700; color: var(--logo-grey);
  }
  .brand-dot { width: 22px; height: 22px; border-radius: 50%; background: var(--logo-grey); }
</style>
</head>
<body>
<div class="flyer">
  <div class="band-warm" role="img" aria-label="Warm orange to olive abstract background with faint angular shapes"></div>
  <svg class="band-cool" width="928" height="450" viewBox="0 0 928 450" aria-hidden="true">
    <defs>
      <linearGradient id="coolGrad" x1="0" y1="0" x2="1" y2="1">
        <stop offset="0" stop-color="#1b6f8f"/>
        <stop offset="0.6" stop-color="#165f7d"/>
        <stop offset="1" stop-color="#0f4a66"/>
      </linearGradient>
    </defs>
    <path d="M0 0H928V420L880 428L760 416L640 432L520 420L400 438L300 424L180 440L60 428L0 436Z" fill="url(#coolGrad)"/>
  </svg>
  <div class="headline-panel"></div>
  <h1 class="headline">Learn how to start<br>your own business<br>out of high school</h1>

  <div class="figure figure--standing-man" role="img" aria-label="Silhouette of a young man standing with arms crossed"></div>
  <div class="figure figure--walking-woman" role="img" aria-label="Silhouette of a young woman standing"></div>
  <div class="figure figure--pair" role="img" aria-label="Small silhouette of two students standing together"></div>

  <ul class="points">
    <li><b>8th</b> graders to <b>12th</b> graders</li>
    <li>Land a <b>REAL JOB</b> internship (instead of Krovetts)</li>
    <li><b>100's</b> of internships available</li>
    <li>Learn how to making <span class="big">way more than minimum wage</span></li>
    <li>In college when interviewing for an internship be the guy that answers <span class="big">"I did an internship before"</span> putting you at a huge advantage</li>
  </ul>

  <div class="footer"></div>
  <p class="cta-lead">Fill in the Contact Us form at</p>
  <div class="url-pill">http://tarnvelsw.com</div>
  <p class="cta-note">at the bottom left corner to find out more information.</p>
  <div class="brand"><span class="brand-dot"></span>Tarnvel Software</div>
</div>
</body>
</html>
```